Pause Your Day And Browse- PYDB poster

I am the Vice President of Advocacy for the Coastline Shelfkeepers Guild. I am looking to have a set of posters made for PYDB (Pause Your Day and Browse) October 23. PYDB is a time when all school children in BC are encouraged to Pause Your Day and Browse for 15-20 minutes at some point in their day.

I would like to get a set of 2 digital posters designed (if possible it would be nice to have the option to print to both 11 x 17 and 8.5 x 11 paper). We need a poster that is high school (Grade 8-12) appropriate and one that is elementary (Grade k-7) appropriate. Both posters need to be replicated in French. All posters need to have the KWNU logo on them as well as the Coastline Shelfkeepers Guild Logo.

Here is a link to last year's successful design http://kwnu-example.org/csg/info/advocacy.html
There are two additional samples in the uploaded files section.

Each poster needs to have the following information:

-Pause Your Day and Browse (PYDB)
- The date Monday, October 23, 2017
-the logo for the KWNU (attached)
-the logo for the CSG (attached)- the logos do not have to be large.

Target Market(s)

Children ages 5-12 and 12-17 as well as their teachers

Industry/Entity Type

Teacher

Font styles to use
Sans Serif

Requirements
Must have
• Must have both logos- colours may be changed for either or both
Nice to have
• Clear, Bright lettering. Images of child or children enjoying reading
Should not have
• stereotypes

```html
<!DOCTYPE html>
<html lang="en">
<head>
<meta charset="utf-8">
<title>Pause Your Day And Browse — PYDB Poster</title>
<link rel="stylesheet" href="https://fonts.googleapis.com/css2?family=Archivo+Black&family=Oswald:wght@600&family=Montserrat:wght@700&display=swap">
<style>
  :root {
    --sky-top: #e48a8c;
    --sky-mid: #eb9886;
    --sky-low: #f2a877;
    --sky-glow: #f8bf73;
    --ink: #0e0a09;
    --paper: #ffffff;
    --guild-green: #2c7a2c;
    --union-blue: #1d3d8a;
  }
  html, body {
    margin: 0;
    padding: 0;
    overflow: hidden;
    background: var(--paper);
  }
  .poster {
    position: relative;
    width: 777px;
    height: 1200px;
    overflow: hidden;
    background: linear-gradient(180deg, var(--sky-top) 0%, var(--sky-mid) 40%, var(--sky-low) 70%, var(--sky-glow) 88%, var(--sky-glow) 100%);
  }
  .reading-scene {
    position: absolute;
    left: 0;
    right: 0;
    top: 800px;
    bottom: 0;
    background: linear-gradient(180deg, rgba(14,10,9,0) 0%, rgba(14,10,9,0.15) 40%, var(--ink) 75%, var(--ink) 100%);
  }
  .title-art {
    position: absolute;
    inset: 0;
    width: 777px;
    height: 1200px;
  }
  .initial {
    font-family: "Archivo Black", "Arial Black", sans-serif;
    font-size: 500px;
    fill: var(--ink);
  }
  .word {
    font-family: "Oswald", "Arial Narrow", sans-serif;
    font-weight: 600;
    font-size: 50px;
    fill: var(--paper);
    text-transform: uppercase;
  }
  .event-date {
    position: absolute;
    left: 0;
    right: 0;
    top: 394px;
    margin: 0;
    text-align: center;
    font-family: "Montserrat", sans-serif;
    font-weight: 700;
    font-size: 41px;
    letter-spacing: 0.5px;
    color: var(--paper);
  }
  .partners {
    position: absolute;
    right: 25px;
    bottom: 14px;
    display: flex;
    gap: 4px;
  }
  .partner {
    width: 66px;
    height: 66px;
    background: var(--paper);
    display: flex;
    align-items: center;
    justify-content: center;
    font-family: "Oswald", "Arial Narrow", sans-serif;
    font-weight: 600;
    font-size: 19px;
  }
  .partner--guild { color: var(--guild-green); }
  .partner--union { color: var(--union-blue); }
</style>
</head>
<body>
<main class="poster">
  <div class="reading-scene" role="img" aria-label="Silhouettes of two children sitting back to back at sunset, one writing and one reading a book"></div>

  <svg class="title-art" viewBox="0 0 777 1200" role="img" aria-label="PYDB — Pause Your Day And Browse">
    <text class="initial" x="62"  y="376" textLength="330" lengthAdjust="spacingAndGlyphs">P</text>
    <text class="initial" x="432" y="376" textLength="272" lengthAdjust="spacingAndGlyphs">Y</text>
    <text class="initial" x="42"  y="812" textLength="362" lengthAdjust="spacingAndGlyphs">D</text>
    <text class="initial" x="436" y="812" textLength="304" lengthAdjust="spacingAndGlyphs">B</text>

    <text class="word" transform="translate(127 364) rotate(-90)">Pause</text>
    <text class="word" transform="translate(507 364) rotate(-90)">Your</text>
    <text class="word" transform="translate(127 800) rotate(-90)">Day</text>
    <text class="word" transform="translate(507 800) rotate(-90)">Browse</text>
  </svg>

  <p class="event-date">MONDAY, OCTOBER 23, 2017</p>

  <div class="partners">
    <div class="partner partner--guild">CSG</div>
    <div class="partner partner--union">KWNU</div>
  </div>
</main>
</body>
</html>
```